Lotus Harmony Massage Facebook Design Project

We need a design to our facebook page for a Thai Massage business located in Houston tx. The current website is lotusharmspa.example.
Updates
Target Market(s)
mostly middle aged from 30-50 25%women 75%men professionals from office to medical to retired
Industry/Entity Type
Business
Colors
Designer to choose colors to be used in the design.
Look and feel
Each slider illustrates characteristics of the customer's brand and the style your logo design should communicate.

```html
<!DOCTYPE html>
<html lang="en">
<head>
<meta charset="utf-8">
<title>Lotus Harmony Massage — Facebook Cover</title>
<link rel="stylesheet" href="https://fonts.googleapis.com/css2?family=Cinzel:wght@400&family=Open+Sans:wght@400&display=swap">
<style>
  :root {
    --red-core: #c93a44;
    --red-mid: #9a1f28;
    --red-deep: #3b0b0d;
    --gold-light: #fbf0b8;
    --gold-mid: #ecd483;
    --gold-edge: #c79f3e;
    --gold-line: #d8b455;
    --name-red: #8e1a1c;
    --url-box: #2a1414;
    --url-text: #e6dcd0;
  }
  * { margin: 0; padding: 0; box-sizing: border-box; }
  html, body {
    width: 1200px;
    height: 448px;
    overflow: hidden;
    background: var(--red-deep);
  }
  .cover {
    position: relative;
    width: 1200px;
    height: 448px;
    overflow: hidden;
  }
  .cover__backdrop {
    position: absolute;
    inset: 0;
    background: radial-gradient(ellipse 70% 80% at 50% 50%, var(--red-core) 0%, var(--red-mid) 55%, var(--red-deep) 100%);
  }
  .banner__rule {
    position: absolute;
    left: 0;
    width: 100%;
    height: 3px;
    background: linear-gradient(90deg, var(--gold-edge), var(--gold-line) 50%, var(--gold-edge));
  }
  .banner__rule--top { top: 130px; }
  .banner__rule--bottom { top: 315px; }
  .banner {
    position: absolute;
    left: 0;
    top: 137px;
    width: 100%;
    height: 173px;
    display: flex;
    align-items: center;
    justify-content: center;
    background: radial-gradient(ellipse 55% 100% at 50% 45%, var(--gold-light) 0%, var(--gold-mid) 65%, var(--gold-edge) 100%);
    box-shadow: 0 2px 6px rgba(0, 0, 0, 0.35);
  }
  .brand__name {
    font-family: "Cinzel", serif;
    font-weight: 400;
    font-size: 54px;
    letter-spacing: 3px;
    line-height: 1;
    color: var(--name-red);
    white-space: nowrap;
  }
  .site-url {
    position: absolute;
    left: 494px;
    top: 413px;
    width: 212px;
    height: 24px;
    background: var(--url-box);
    font-family: "Open Sans", sans-serif;
    font-size: 13px;
    line-height: 24px;
    text-align: center;
    color: var(--url-text);
  }
</style>
</head>
<body>
  <main class="cover">
    <div class="cover__backdrop" role="img" aria-label="Deep red background with a darker red swirling damask floral pattern"></div>
    <div class="banner__rule banner__rule--top"></div>
    <section class="banner">
      <h1 class="brand__name">Lotus Harmony Massage</h1>
    </section>
    <div class="banner__rule banner__rule--bottom"></div>
    <p class="site-url">www.lotusharmspa.example</p>
  </main>
</body>
</html>
```